Business card for a business coach / management consultant

My logo has been done and now I need a business card. Deliverable needs to be a PDF to give to the printer. I want it single sided as I want the back side blank.
I prefer a white card with modern simple professional design.
Details are:
Dale Whitford
B.Sc. (hons) FRLT CP MNBQR
7 Corrigan Rd
Brindle Park WA 6093
Australia
mobile 040 31 582 47
email dale@ventureharbor.example.au
skype dalewhitfordnorth
Small to medium size business owners
Business

```html
<!DOCTYPE html>
<html lang="en">
<head>
<meta charset="utf-8">
<title>Dale Whitford — Business Card</title>
<link rel="stylesheet" href="https://fonts.googleapis.com/css2?family=Oswald:wght@400;600;700&family=Open+Sans:wght@700&display=swap">
<style>
  :root {
    --backdrop: #6f6f71;
    --card: #f7f7f5;
    --brand-blue: #2a5a9c;
    --stripe-blue: #33609f;
    --ink-grey: #707276;
  }
  html, body {
    margin: 0;
    width: 1200px;
    height: 1000px;
    overflow: hidden;
    background: var(--backdrop);
  }
  .business-card {
    position: absolute;
    left: 150px;
    top: 243px;
    width: 900px;
    height: 514px;
    background: var(--card);
    box-shadow: 0 6px 24px rgba(0,0,0,0.35);
    overflow: hidden;
  }
  .edge-stripe {
    position: absolute;
    left: 0; top: 0;
    width: 12px; height: 100%;
    background: var(--stripe-blue);
  }
  .holder-name {
    position: absolute;
    left: 34px; top: 22px;
    margin: 0;
    font-family: "Oswald", sans-serif;
    font-weight: 700;
    font-size: 120px;
    line-height: 1;
    letter-spacing: 3px;
    color: var(--brand-blue);
    text-transform: uppercase;
    white-space: nowrap;
  }
  .contact-list {
    position: absolute;
    left: 170px; top: 162px;
    margin: 0; padding: 0;
    list-style: none;
    font-family: "Oswald", sans-serif;
    font-weight: 400;
    text-transform: uppercase;
    color: var(--ink-grey);
  }
  .contact-list li { line-height: 1.25; }
  .contact-email { font-size: 20px; }
  .contact-skype { font-size: 22px; }
  .contact-skype .label { color: var(--brand-blue); font-weight: 600; }
  .contact-phone { font-size: 30px; letter-spacing: 2px; }
  .credentials {
    position: absolute;
    right: 34px; top: 178px;
    margin: 0;
    font-family: "Oswald", sans-serif;
    font-size: 22px;
    color: var(--ink-grey);
    letter-spacing: 1px;
    text-transform: uppercase;
  }
  .credentials .bracket { color: var(--brand-blue); font-weight: 700; }
  .brand-mark {
    position: absolute;
    left: 40px; top: 370px;
    display: flex;
    align-items: center;
    gap: 16px;
  }
  .brand-dot {
    width: 52px; height: 52px;
    border-radius: 50%;
    background: var(--brand-blue);
  }
  .brand-name {
    font-family: "Open Sans", sans-serif;
    font-weight: 700;
    font-size: 40px;
    color: var(--brand-blue);
  }
  .postal-address {
    position: absolute;
    left: 530px; top: 390px;
    margin: 0;
    font-family: "Oswald", sans-serif;
    font-style: normal;
    font-size: 22px;
    line-height: 1.35;
    letter-spacing: 1px;
    color: var(--ink-grey);
    text-transform: uppercase;
  }
</style>
</head>
<body>
  <section class="business-card">
    <div class="edge-stripe"></div>
    <h1 class="holder-name">Dale Whitford</h1>
    <ul class="contact-list">
      <li class="contact-email">dale@ventureharbor.example.au</li>
      <li class="contact-skype"><span class="label">Skype:</span>dalewhitfordnorth</li>
      <li class="contact-phone">040 31 582 47</li>
    </ul>
    <p class="credentials"><span class="bracket">[</span>B.Sc. (Hons) FRLT CP MNBQR<span class="bracket">]</span></p>
    <div class="brand-mark">
      <span class="brand-dot"></span>
      <span class="brand-name">Orvelle Advisory</span>
    </div>
    <address class="postal-address">7 Corrigan Rd<br>Brindle Park WA 6093, Australia</address>
  </section>
</body>
</html>
```